Clear Road Rentals flyer

Need a A6 size horizontal layout flyer. See attached example for ideas as well as some images I have which you can use. we are a hire car company that provides vehicles to clients who have recently been involved in car accidents and who's cars are currently getting fixed and so they lose the use of their own vehicle. see our website to keep flyer in line with website and for any further information clearroadrentals.com.au

Target Market(s)

people involved in not at fault car accidents

Industry/Entity Type

It Company

Requirements
Must have
• *ask people to let us know where they got our flyer from when they call us
• *call to action for people to call our phone number 1800 452 817
Should not have
• any mentioning that the vehicle is free

```html
<!DOCTYPE html>
<html lang="en">
<head>
<meta charset="utf-8">
<title>Clear Road Rentals – Accident Replacement Car Flyer</title>
<link rel="stylesheet" href="https://fonts.googleapis.com/css2?family=Lato:wght@400;700&family=Montserrat:wght@700&family=Roboto+Condensed:wght@700&family=Roboto:wght@300;400;700&display=swap">
<style>
  :root {
    --blue: #3b93f0;
    --yellow: #fdb913;
    --charcoal: #3d3d41;
    --charcoal-dark: #2f2f33;
    --ink: #2b2b2b;
    --text-grey: #4a4a4a;
    --white: #ffffff;
    --page: #ececec;
  }
  * { box-sizing: border-box; margin: 0; padding: 0; }
  html, body { width: 927px; height: 1200px; overflow: hidden; }
  body { background: var(--page); position: relative; font-family: "Lato", sans-serif; }

  .flyer {
    position: absolute; left: 113px; width: 700px; height: 496px;
    overflow: hidden; box-shadow: 0 3px 12px rgba(0,0,0,.25);
  }
  .flyer--front { top: 80px; background: var(--white); }
  .flyer--back { top: 624px; background: var(--charcoal); }

  /* front */
  .hero-photo {
    position: absolute; left: 0; top: 0; width: 700px; height: 346px;
    background: linear-gradient(100deg, #5b6470 0%, #9aa3ad 35%, #c9c4bd 60%, #7a6f72 85%, #a05a63 100%);
  }
  .accent-bar { position: absolute; top: 346px; height: 12px; }
  .accent-bar--blue { left: 0; width: 359px; background: var(--blue); }
  .accent-bar--dark { left: 359px; width: 341px; background: var(--charcoal); }

  .brand-name {
    position: absolute; font-family: "Lato", sans-serif; font-weight: 700;
    display: flex; align-items: center; gap: 8px; white-space: nowrap;
  }
  .brand-name__dot { width: 14px; height: 14px; border-radius: 50%; }
  .flyer--front .brand-name { right: 30px; top: 96px; color: var(--white); font-size: 22px; }
  .flyer--front .brand-name__dot { background: var(--white); }

  .headline-box {
    position: absolute; left: 359px; top: 176px; width: 341px; height: 147px;
    background: var(--blue); padding: 18px 0 0 17px;
  }
  .headline-box h1 {
    font-family: "Roboto Condensed", sans-serif; font-weight: 700; color: var(--white);
    font-size: 33px; line-height: 33px; letter-spacing: .6px;
  }
  .headline-box p {
    margin-top: 9px; font-family: "Roboto Condensed", sans-serif; font-weight: 700;
    color: var(--charcoal-dark); font-size: 15.5px; line-height: 20px; letter-spacing: .4px;
  }

  .phone-mockup {
    position: absolute; left: 29px; top: 249px; width: 171px; height: 247px;
    border-radius: 22px 22px 0 0;
    background: linear-gradient(180deg, #2a2a2d 0%, #2a2a2d 18%, #3b93f0 18%, #3b93f0 45%, #f4f6f8 45%, #e8eef6 100%);
  }

  .intro-text {
    position: absolute; left: 223px; top: 380px; width: 460px;
    font-size: 12px; line-height: 17px; color: var(--text-grey); letter-spacing: -.1px;
  }
  .web-pill {
    position: absolute; left: 223px; top: 441px; width: 453px; height: 37px;
    background: var(--charcoal); border-radius: 8px;
    display: flex; align-items: center; justify-content: center; gap: 6px;
    font-family: "Montserrat", sans-serif; font-weight: 700; font-size: 16px; color: var(--white);
  }
  .web-pill a { color: var(--blue); text-decoration: none; }

  /* back */
  .process-box {
    position: absolute; left: 17px; top: 0; width: 325px; height: 177px;
    background: var(--yellow); padding: 26px 20px 0 24px;
    font-weight: 700; color: var(--white); font-size: 14.3px; line-height: 21.6px;
  }
  .car-photo {
    position: absolute; left: 342px; top: 22px; width: 358px; height: 148px;
    background: linear-gradient(90deg, #3a3b36 0%, #6d6f68 35%, #cfd3d6 60%, #e9ecee 80%, #b8bcc0 100%);
  }
  .section-tab {
    position: absolute; left: 0; top: 203px; width: 206px; height: 31px;
    background: var(--blue); color: var(--white);
    font-family: "Montserrat", sans-serif; font-weight: 700; font-size: 18px;
    display: flex; align-items: center; padding-left: 29px; letter-spacing: .4px;
  }
  .step { position: absolute; top: 265px; display: flex; gap: 14px; }
  .step--one { left: 31px; }
  .step--two { left: 255px; }
  .step--three { left: 468px; }
  .step__icon {
    width: 82px; height: 82px; border-radius: 50%; background: var(--white);
    border: 5px solid var(--yellow); flex: none;
    display: flex; align-items: center; justify-content: center;
  }
  .step__label {
    font-family: "Roboto Condensed", sans-serif; font-weight: 700; color: var(--yellow);
    font-size: 18px; margin-top: -4px;
  }
  .step__body {
    font-family: "Roboto", sans-serif; font-weight: 300; color: var(--white);
    font-size: 16.5px; line-height: 19px; margin-top: 3px;
  }

  .contact-band {
    position: absolute; left: 0; top: 389px; width: 308px; height: 107px;
    background: var(--blue); color: var(--white); padding: 16px 0 0 32px;
  }
  .contact-band__phone {
    font-family: "Roboto", sans-serif; font-weight: 700; font-size: 35px; line-height: 38px; letter-spacing: .8px;
  }
  .contact-band__web {
    font-family: "Roboto", sans-serif; font-weight: 700; font-size: 17px; line-height: 22px;
  }
  .contact-band__source {
    font-family: "Roboto", sans-serif; font-weight: 400; font-size: 11.5px; line-height: 16px; margin-top: 3px;
  }
  .brand-band {
    position: absolute; left: 308px; top: 389px; width: 392px; height: 107px; background: var(--white);
  }
  .tagline {
    position: absolute; left: 22px; top: 31px; width: 176px; text-align: center;
    font-family: "Roboto Condensed", sans-serif; font-weight: 700; color: var(--blue);
    font-size: 14px; line-height: 17px;
  }
  .brand-band .brand-name { right: 18px; top: 40px; color: var(--ink); font-size: 18px; }
  .brand-band .brand-name__dot { background: var(--blue); }
</style>
</head>
<body>

<section class="flyer flyer--front">
  <div class="hero-photo" role="img" aria-label="Photo of a smiling senior man at the wheel of a car with a smiling woman in the passenger seat"></div>
  <div class="accent-bar accent-bar--blue"></div>
  <div class="accent-bar accent-bar--dark"></div>

  <div class="brand-name"><span class="brand-name__dot"></span>Clear Road Rentals</div>

  <div class="headline-box">
    <h1>ACCIDENT<br>REPLACEMENT CAR</h1>
    <p>WE GET DRIVERS BACK ON THE ROAD<br>AFTER CAR ACCIDENTS EVERYDAY</p>
  </div>

  <div class="phone-mockup" role="img" aria-label="Smartphone showing the company website home page"></div>

  <p class="intro-text">If the accident wasn't your fault, an accident replacement vehicle is available to you. You can call and schedule this replacement car so that you are not left without a car while it is under repairs.</p>

  <div class="web-pill">Visit our website <a href="#">www.clearroadrentals.com.au</a></div>
</section>

<section class="flyer flyer--back">
  <div class="process-box">It's a Simple Process. Getting an accident replacement car is easier than you might think. As long as you can provide us with all requested accident details and parties involved details, we can handle the rest of the process.</div>
  <div class="car-photo" role="img" aria-label="Close-up photo of the front headlight of a white car on a shaded road"></div>

  <div class="section-tab">HOW IT WORKS</div>

  <div class="step step--one">
    <div class="step__icon">
      <svg width="38" height="38" viewBox="0 0 38 38" fill="none" stroke="#3d3d41" stroke-width="2" stroke-linecap="round" stroke-linejoin="round">
        <path d="M27 20V6H8v27h12"/><path d="M12 12h11M12 17h11M12 22h6"/><path d="M22 29l4 4 8-9"/>
      </svg>
    </div>
    <div>
      <div class="step__label">STEP 1</div>
      <div class="step__body">Call us on<br>1800 452 817<br>Free call</div>
    </div>
  </div>

  <div class="step step--two">
    <div class="step__icon">
      <svg width="40" height="40" viewBox="0 0 40 40" fill="none" stroke="#3d3d41" stroke-width="2" stroke-linecap="round" stroke-linejoin="round">
        <path d="M8 14c0 9 8 18 17 20l4-4-5-5-3 2c-3-2-6-5-7-8l2-3-5-5z"/>
        <circle cx="27" cy="12" r="8"/><path d="M22 19l-2 3 4-1"/>
        <circle cx="24" cy="12" r=".6" fill="#3d3d41"/><circle cx="27" cy="12" r=".6" fill="#3d3d41"/><circle cx="30" cy="12" r=".6" fill="#3d3d41"/>
      </svg>
    </div>
    <div>
      <div class="step__label">STEP 2</div>
      <div class="step__body">Provide<br>accident<br>details</div>
    </div>
  </div>

  <div class="step step--three">
    <div class="step__icon">
      <svg width="44" height="30" viewBox="0 0 44 30" fill="none" stroke="#3d3d41" stroke-width="2" stroke-linecap="round" stroke-linejoin="round">
        <path d="M4 21v-6l4-2 5-8h17l6 8 4 2v6h-4"/><path d="M8 21H4M15 21h14"/>
        <path d="M14 13l3-5h5v5zM25 13V8h4l3 5z"/>
        <circle cx="11.5" cy="22" r="3.5"/><circle cx="32.5" cy="22" r="3.5"/>
      </svg>
    </div>
    <div>
      <div class="step__label">STEP 3</div>
      <div class="step__body">You get a<br>replacement<br>vehicle</div>
    </div>
  </div>

  <div class="contact-band">
    <div class="contact-band__phone">1800 452 817</div>
    <div class="contact-band__web">www.clearroadrentals.com.au</div>
    <div class="contact-band__source">When you call, tell us where you found this flyer.</div>
  </div>
  <div class="brand-band">
    <div class="tagline">AUSTRALIA'S NO.1<br>CAR ACCIDENT<br>REPLACEMENT SERVICE</div>
    <div class="brand-name"><span class="brand-name__dot"></span>Clear Road Rentals</div>
  </div>
</section>

</body>
</html>
```